A new PowerPoint Template for a French consulting company

Who are we?

Formed in 2005, Quorv is a consulting company specialising in the human aspect of change and transformation.

From our offices in the heart of Paris, our team of 30 consultants work with leading organisations in the Aerospace, Finance, Transportation and Public sectors to deliver lasting change.

Our customers trust us with some of their most strategic and sensitive projects. They trust us with these projects because:
- We listen to them, ensuring we understand the real needs of their business
- We involve them, co-developing and tailoring our solutions to the specific challenges they face
- We’re professional, without taking ourselves too seriously
- We’re imaginative, whilst always remaining pragmatic
- We get results!

You can find out more about who we are and the work we do here: http://www.quorv-example.fr/en

What we need from you?

We’re approaching our 10th birthday and, whilst we still love what we do, we think it’s the right time to update our image.

We’d like you to design us a new PowerPoint template, that will be used for all of our internal and client facing work. You can base your submissions on our existing logo and colour scheme (see files attached) or you can submit your own fresh ideas – after all, we’re not afraid of change!

Finally, whilst we’re looking for you to be creative, there are some simple guidelines that we need you to keep in mind:

1. The Template needs to include both a front cover and a “content” page

2. The front cover needs to:
- Include our logo
- Reflect “who we are” and the type of work that we do

3. The content page needs to:
- Have a predominantly white background
- Be practical to use, making an effective use of the 4:3 standard PPT size
- Include an area across the top of the page for the slide title
- Include areas along the bottom of the page for the page number and date

4. If you decide to propose a new colour scheme, it should be balanced and the “accents” usable

5. The PowerPoint Template needs to be “printer friendly”

6. The fonts you use should be standard

What we don’t want?

To give you as much help as possible, here are some things that we really don’t want:

- Submissions that are dull grey or navy blue, suggesting we’re nothing but boring corporate suits
- Submissions that are Lulette pink or too “soft and cuddly”
- Submissions that use lots of stock images of “happy, smiling, consultants”
- Submissions that will be the height of fashion today, but completely out of date next year

```html
<!DOCTYPE html>
<html lang="en">
<head>
<meta charset="utf-8">
<title>Quorv – Closing Slide</title>
<link href="https://fonts.googleapis.com/css2?family=Carlito:wght@400;700&display=swap" rel="stylesheet">
<style>
  :root {
    --plum: #5c0035;
    --teal: #2bb1a6;
    --grey: #555555;
    --paper: #ffffff;
  }
  html, body {
    margin: 0;
    padding: 0;
    overflow: hidden;
    background: var(--paper);
  }
  .slide {
    position: relative;
    width: 1200px;
    height: 900px;
    overflow: hidden;
    background: var(--paper);
    font-family: "Carlito", "Calibri", sans-serif;
  }
  .accent-bar {
    position: absolute;
    top: 0;
    left: 0;
    width: 100%;
    height: 9px;
    display: flex;
  }
  .accent-bar__plum { width: 602px; background: var(--plum); }
  .accent-bar__teal { flex: 1; background: var(--teal); }

  .brand {
    position: absolute;
    left: 0;
    width: 100%;
    top: 330px;
    text-align: center;
  }
  .brand__lockup {
    display: inline-block;
    text-align: right;
  }
  .brand__name {
    margin: 0;
    font-size: 110px;
    font-weight: 700;
    line-height: 1;
    color: var(--plum);
    letter-spacing: -1px;
  }
  .brand__tagline {
    margin: 14px 2px 0 0;
    font-size: 27px;
    font-weight: 400;
    line-height: 1;
    color: var(--teal);
  }

  .contact {
    position: absolute;
    top: 515px;
    left: 0;
    width: 100%;
    display: grid;
    grid-template-columns: 538px auto;
    column-gap: 10px;
    row-gap: 6px;
    align-items: baseline;
  }
  .contact__label {
    text-align: right;
    font-size: 19px;
    color: var(--plum);
  }
  .contact__value {
    font-size: 22px;
    color: var(--grey);
  }
</style>
</head>
<body>
  <main class="slide">
    <div class="accent-bar">
      <div class="accent-bar__plum"></div>
      <div class="accent-bar__teal"></div>
    </div>

    <section class="brand">
      <div class="brand__lockup">
        <h1 class="brand__name">Quorv</h1>
        <p class="brand__tagline">guiding change</p>
      </div>
    </section>

    <section class="contact">
      <span class="contact__label">website:</span>
      <span class="contact__value">www.yourdomain.com</span>
      <span class="contact__label">Phone:</span>
      <span class="contact__value">612-4478019-30571</span>
    </section>
  </main>
</body>
</html>
```